Bramblefield Circle for Nurses - New facebook banner design + logo

We are setting up a new private facebook group called Bramblefield Circle for Nurses. Administered by Marla Teske, Marla helps women in healthcare to crush their life and health goals so they can bring their best version of themselves to others. We would like a modern / contemporary header design incorporating colours / fonts from the attached moodboard. An icon or image representing a woman. Our initial thinking included an icon of a woman outline? Just thoughts. Bright bold colours incorporating some gold / marble. See existing business brandboard however elements of Bramblefield Circle for Nurses DO NOT need to be aligned to this brandboard. Images should represent personal strength (not physical strength ie. fitness), community and femininity.

Target Market(s)

Women in healthcare

Industry/Entity Type

Healthcare

Font styles to use
Sans Serif

Requirements
Must have
• unique iconology that can be used to represent the group. I've attached some examples of woman silhouettes. Doesn't need to be full body but iconology may just include head / shoulders / torso.

```html
<!DOCTYPE html>
<html lang="en">
<head>
<meta charset="utf-8">
<title>Bramblefield Circle for Nurses — Group Banner</title>
<link rel="stylesheet" href="https://fonts.googleapis.com/css2?family=Montserrat:wght@300;400;700&display=swap">
<style>
  :root {
    --marble-light: #f4f4f4;
    --marble-mid: #d9d9da;
    --marble-vein: #b9babc;
    --teal: #3fe0d8;
    --teal-soft: #8ef0ea;
    --orange: #ff8a2b;
    --orange-deep: #f47a1c;
    --ink: #111111;
    --suit: #1b1c20;
    --suit-light: #3a3b40;
  }
  * { margin: 0; padding: 0; box-sizing: border-box; }
  html, body { width: 1200px; height: 457px; overflow: hidden; background: var(--marble-light); }
  .banner {
    position: relative;
    width: 1200px;
    height: 457px;
    overflow: hidden;
    font-family: "Montserrat", sans-serif;
    color: var(--ink);
  }
  .marble {
    position: absolute; inset: 0;
    background:
      linear-gradient(125deg, transparent 30%, rgba(185,186,188,0.35) 38%, transparent 46%),
      linear-gradient(60deg, transparent 55%, rgba(185,186,188,0.3) 62%, transparent 70%),
      linear-gradient(160deg, var(--marble-light) 0%, var(--marble-mid) 45%, var(--marble-light) 70%, var(--marble-mid) 100%);
  }
  .brush { position: absolute; }
  .brush--teal { left: 0; top: 0; width: 280px; height: 350px; }
  .brush--orange { right: 0; bottom: 0; width: 215px; height: 295px; }
  .portrait {
    position: absolute;
    left: 755px; top: 52px;
    width: 262px; height: 405px;
    border-radius: 120px 120px 0 0;
    background: linear-gradient(180deg, #c8a27a 0%, #e7c7ad 28%, var(--suit-light) 45%, var(--suit) 100%);
  }
  .title {
    position: absolute;
    left: 198px; top: 122px;
    width: 520px;
    text-align: center;
    text-transform: uppercase;
    line-height: 1;
  }
  .title__line {
    display: block;
    font-size: 50px;
    letter-spacing: 5px;
    margin-bottom: 16px;
  }
  .title__bold { font-weight: 700; }
  .title__light { font-weight: 300; }
</style>
</head>
<body>
  <main class="banner">
    <div class="marble" role="img" aria-label="White and grey marble texture background"></div>

    <svg class="brush brush--teal" viewBox="0 0 280 350" role="img" aria-label="Teal painted brush stroke">
      <defs>
        <linearGradient id="tealFill" x1="0" y1="0" x2="1" y2="1">
          <stop offset="0" stop-color="var(--teal)"/>
          <stop offset="1" stop-color="var(--teal-soft)"/>
        </linearGradient>
      </defs>
      <path d="M0 0 H250 C275 40 270 110 240 170 C210 240 150 300 70 335 C40 347 15 345 0 340 Z" fill="url(#tealFill)"/>
    </svg>

    <svg class="brush brush--orange" viewBox="0 0 215 295" role="img" aria-label="Orange painted brush stroke">
      <path d="M60 20 C110 0 180 -5 215 10 V295 H5 C0 240 10 180 20 120 C28 70 35 35 60 20 Z" fill="var(--orange)"/>
    </svg>

    <div class="portrait" role="img" aria-label="Photo of a smiling businesswoman in glasses and a dark suit with arms crossed"></div>

    <h1 class="title">
      <span class="title__line title__bold">Bramblefield</span>
      <span class="title__line title__light">Circle for</span>
      <span class="title__line title__bold">Nurses</span>
    </h1>
  </main>
</body>
</html>
```